Company business card

We need a new business card design. We are IT company which is specialized for outsourcing of operations hardware and software (specially Velbrandt, we are a partner), developing custom applications and web applications, BPM solutions, auditing hw and sw. actually design was attached. But we need completely NEW.

Industry/Entity Type

Business

```html
<!DOCTYPE html>
<html lang="en">
<head>
<meta charset="utf-8">
<title>KORVEN – Business Card</title>
<link rel="stylesheet" href="https://fonts.googleapis.com/css2?family=Open+Sans:wght@400;600;700;800&display=swap">
<style>
  :root {
    --backdrop: #8a8a8a;
    --brand-blue: #1f78c1;
    --brand-blue-deep: #1a68a9;
    --header-dark: #333333;
    --ink: #1d1d1d;
    --ink-soft: #4a4a4a;
    --card-white: #ffffff;
    --card-tint: #a9c3d6;
    --shadow: rgba(0, 0, 0, 0.35);
  }
  * { box-sizing: border-box; margin: 0; padding: 0; }
  html, body {
    width: 1200px; height: 768px; overflow: hidden;
    background: var(--backdrop);
    font-family: "Open Sans", Arial, sans-serif;
  }
  .canvas { position: relative; width: 1200px; height: 768px; }

  .card {
    position: absolute; width: 520px; height: 297px;
    box-shadow: 0 10px 24px var(--shadow);
    overflow: hidden;
  }

  /* Back side */
  .card-back { left: 50px; top: 236px; background: var(--brand-blue); }
  .card-back .back-texture { position: absolute; inset: 0; background: linear-gradient(160deg, var(--brand-blue) 0%, var(--brand-blue-deep) 100%); }
  .back-mark {
    position: absolute; left: 50%; top: 92px; transform: translateX(-50%);
    width: 110px; height: 94px; background: var(--card-white);
    display: flex; flex-direction: column; align-items: center; justify-content: center; gap: 8px;
  }
  .back-mark .mark-square { width: 22px; height: 22px; background: var(--brand-blue); }
  .back-mark .mark-name { font-weight: 800; font-size: 20px; color: var(--brand-blue); letter-spacing: 0.5px; }
  .back-url {
    position: absolute; top: 194px; width: 100%; text-align: center;
    color: var(--card-white); font-size: 11px; letter-spacing: 2px;
  }

  /* Front side */
  .card-front {
    left: 630px; top: 236px;
    background: linear-gradient(100deg, var(--card-white) 0%, var(--card-white) 38%, var(--card-tint) 100%);
  }
  .front-texture {
    position: absolute; right: 0; top: 0; width: 55%; height: 100%;
    background: linear-gradient(100deg, rgba(169,195,214,0) 0%, rgba(140,172,196,0.35) 100%);
  }
  .side-strip { position: absolute; left: 40px; top: 0; width: 58px; height: 100%; background: var(--brand-blue); }
  .strip-header { height: 16px; background: var(--header-dark); }
  .strip-mark { height: 64px; border-bottom: 2px solid var(--card-white); display: flex; align-items: center; justify-content: center; }
  .strip-mark .mark-square { width: 30px; height: 30px; background: var(--card-white); }
  .strip-icon { position: absolute; left: 21px; width: 16px; height: 16px; }

  .brand-name {
    position: absolute; left: 112px; top: 26px;
    font-weight: 800; font-size: 40px; line-height: 1; color: var(--ink); letter-spacing: 0.5px;
  }
  .contact { position: absolute; left: 112px; top: 104px; color: var(--ink-soft); font-size: 12px; line-height: 1.35; }
  .person-name { font-weight: 700; font-size: 18px; color: var(--brand-blue); line-height: 1.2; }
  .person-role { margin-bottom: 14px; color: var(--ink); }
  .company-block { margin-bottom: 12px; }
  .contact p { white-space: nowrap; }
</style>
</head>
<body>
<main class="canvas">

  <section class="card card-back" aria-label="Business card back">
    <div class="back-texture" role="img" aria-label="Blue background with faint binary digit pattern"></div>
    <div class="back-mark">
      <span class="mark-square"></span>
      <span class="mark-name">KORVEN</span>
    </div>
    <p class="back-url">www.korven.sk</p>
  </section>

  <section class="card card-front" aria-label="Business card front">
    <div class="front-texture" role="img" aria-label="Faint binary digit pattern on light blue"></div>

    <div class="side-strip">
      <div class="strip-header"></div>
      <div class="strip-mark"><span class="mark-square"></span></div>

      <svg class="strip-icon" style="top:108px" viewBox="0 0 16 16" aria-hidden="true">
        <circle cx="8" cy="5" r="3.2" fill="#fff"/>
        <path d="M2 15c0-3.5 2.7-5.5 6-5.5s6 2 6 5.5z" fill="#fff"/>
      </svg>
      <svg class="strip-icon" style="top:142px" viewBox="0 0 16 16" aria-hidden="true">
        <path d="M8 1a5 5 0 0 0-5 5c0 4 5 9 5 9s5-5 5-9a5 5 0 0 0-5-5z" fill="#fff"/>
        <circle cx="8" cy="6" r="1.8" fill="#1f78c1"/>
      </svg>
      <svg class="strip-icon" style="top:190px" viewBox="0 0 16 16" aria-hidden="true">
        <rect x="4" y="1" width="8" height="14" rx="1.5" fill="none" stroke="#fff" stroke-width="1.5"/>
        <circle cx="8" cy="12.5" r="0.9" fill="#fff"/>
      </svg>
      <svg class="strip-icon" style="top:210px" viewBox="0 0 16 16" aria-hidden="true">
        <rect x="1.5" y="3.5" width="13" height="9" fill="#fff"/>
        <path d="M1.5 3.5 8 9l6.5-5.5" fill="none" stroke="#1f78c1" stroke-width="1.2"/>
      </svg>
      <svg class="strip-icon" style="top:230px" viewBox="0 0 16 16" aria-hidden="true">
        <circle cx="8" cy="8" r="6.2" fill="#fff"/>
        <path d="M2 8h12M8 2c-2.5 3-2.5 9 0 12M8 2c2.5 3 2.5 9 0 12" fill="none" stroke="#1f78c1" stroke-width="1"/>
      </svg>
    </div>

    <h1 class="brand-name">KORVEN</h1>

    <div class="contact">
      <p class="person-name">Marek Halvik</p>
      <p class="person-role">CEO</p>
      <div class="company-block">
        <p>KORVEN s.r.o.</p>
        <p>Javorová 18, 811 04 Bratislava</p>
      </div>
      <p>+421 (0) 900 123 456</p>
      <p>marek.halvik@korven.sk</p>
      <p>www.korven.sk</p>
    </div>
  </section>

</main>
</body>
</html>
```